Learning Horizon Collective Website

Background

Learning Horizon Collective (LHC) is a newly established consultancy that focuses on education, primarily improving schools and universities. The company is registered in Dubai.

Domain name is learnhorizonco.com, the logo for LHC is attached as is the registered business address

Scope

LHC requests designers to design and build a website that initially includes the following key pages/sections.

• About us/our story
• Our people
• Our services
• Our work
• Contact us/social media

Some examples of websites that are similar to the look and feel of a new contemporary startup like LHC include the following:
http://www.telvano.co/journal/
https://www.quorimadvisory.com/

Content to be provided by LHC. In addition, LHC wishes the successful designer to set up all email and social media accounts required.

Target Market(s)

Government Education departments, donors, Private school chains, school owners, NGOs, investors

Industry/Entity Type

Education

Number of Pages Required

3 page

Font styles to use
Sans Serif

Colors

Designer to choose colors to be used in the design.

Requirements
Must have
• • About us/our story
• • Our people
• • Our services
• • Our work
• • Contact us/social media
• (Maximum 3 pages)
• domain name, address, our services etc
• Blend colours with logo design colours
Nice to have
• Given the migration to mobile devices, we think that having a site which can be scrolled from top to bottom would be preferable
• Possibly a lite version in areas where bandwidth is poor?
Should not have
• Anything that takes a long time to download

```html
<!DOCTYPE html>
<html lang="en">
<head>
<meta charset="utf-8">
<title>Learning Horizon Collective</title>
<link rel="stylesheet" href="https://fonts.googleapis.com/css2?family=Montserrat:ital,wght@0,400;0,500;0,600;1,400;1,600&display=swap">
<style>
:root{
  --navy:#3a4d9a;
  --teal:#2ba3c4;
  --ink:#3b3b3b;
  --muted:#6d6d6d;
  --light:#f1f1f1;
  --topbar:#2f2f2f;
  --footer:#262626;
  --footer-base:#1b1b1b;
  --white:#ffffff;
}
*{margin:0;padding:0;box-sizing:border-box}
html,body{width:1200px;height:2980px;overflow:hidden}
body{position:relative;font-family:"Montserrat",Arial,sans-serif;color:var(--ink);background:var(--white)}
.abs{position:absolute}
.topbar{left:0;top:0;width:1200px;height:30px;background:var(--topbar);color:#d8d8d8;font-size:11px}
.topbar .address{left:56px;top:8px;display:flex;align-items:center;gap:10px}
.topbar .social{right:46px;top:7px;display:flex;gap:8px}
.topbar .social span{width:14px;height:14px;border-radius:50%;display:block}
.header{left:0;top:30px;width:1200px;height:82px;background:var(--white)}
.brand{left:56px;top:24px;display:flex;align-items:center;gap:12px;color:var(--navy);font-weight:600;font-size:24px}
.brand .mark{width:30px;height:30px;background:var(--teal)}
.nav{right:46px;top:31px;display:flex;gap:58px;font-size:15px;color:#444}
.hero{left:0;top:112px;width:1200px;height:444px;background:linear-gradient(100deg,#5d4a3a 0%,#8a7560 35%,#7f8a86 60%,#6b6f72 100%)}
.hero h1{left:56px;top:106px;color:var(--white);font-weight:500;font-size:35px;line-height:54px}
.btn{display:flex;align-items:center;justify-content:center;border-radius:6px;font-size:20px;font-weight:500}
.btn-fill{background:var(--navy);color:var(--white)}
.hero .btn{left:56px;top:252px;width:198px;height:46px}
.dots{left:570px;top:408px;display:flex;gap:8px}
.dots span{width:7px;height:7px;border-radius:50%;background:rgba(255,255,255,.5)}
.dots span.on{background:var(--white)}
.services{left:0;top:556px;width:1200px;height:512px;background:var(--light)}
.section-title{font-size:30px;font-weight:600;color:#444}
.services .section-title{left:0;width:1200px;top:30px;text-align:center}
.rule{height:3px;width:60px;background:var(--teal)}
.services .rule{left:570px;top:80px}
.services .intro{left:220px;width:760px;top:96px;text-align:center;font-size:14px;line-height:24px;color:var(--muted)}
.service{top:186px;width:260px;text-align:center;font-size:17px;line-height:24px;color:#333}
.service svg{display:block;margin:0 auto 28px;height:116px}
.services .btn{left:495px;top:419px;width:211px;height:51px;font-size:22px}
.mission h2{left:56px;top:1100px;font-size:34px;font-weight:500;line-height:44px;color:#333}
.mission .body{left:56px;top:1212px;width:520px;font-size:18px;line-height:35px;color:var(--muted)}
.mission .countries{left:56px;top:1364px;width:540px;font-size:18px;line-height:35px;font-style:italic;font-weight:600;color:#444}
.btn-line{border:2px solid var(--navy);color:var(--navy);background:var(--white);border-radius:8px}
.mission .btn{left:56px;top:1502px;width:212px;height:51px;font-size:22px}
.mission .photo{left:678px;top:1104px;width:468px;height:448px;background:linear-gradient(135deg,#c9c2b3 0%,#8c8676 45%,#2e2e2e 100%)}
.band{left:0;top:1586px;width:1200px;height:348px;background:linear-gradient(90deg,#3a3a3a,#4d4a47 50%,#3b3b3b);color:var(--white);text-align:center}
.band h2{left:0;width:1200px;top:80px;font-size:38px;font-weight:500}
.band p{left:0;width:1200px;top:146px;font-size:19px}
.band .btn{left:495px;top:214px;width:211px;height:52px;font-size:19px;border-radius:5px}
.people .section-title{left:56px;top:1970px;font-size:29px}
.people .rule{left:56px;top:2018px}
.arrow-btn{top:1994px;width:54px;height:22px;border:2px solid #999;border-radius:9px;display:flex;align-items:center;justify-content:center}
.tabs{left:308px;top:2044px;display:flex;gap:56px;font-size:16px;color:#aaa}
.tabs .active{color:var(--teal)}
.feature-bg{left:56px;top:2136px;width:442px;height:388px;background:var(--light)}
.feature-photo{left:56px;top:2108px;width:400px;height:252px;background:linear-gradient(160deg,#7c8f82 0%,#a9a79c 50%,#d8d2c6 100%)}
.quote{font-size:18px;line-height:28px;color:var(--muted)}
.name{font-style:italic;font-size:19px;color:var(--teal)}
.feature-quote{left:80px;top:2392px;width:380px}
.feature-name{left:84px;top:2462px}
.thumb{left:602px;width:152px;height:116px}
.person-quote{left:810px;width:350px}
.footer{left:0;top:2564px;width:1200px;height:364px;background:var(--footer);color:#cfcfcf}
.footer .brand{left:56px;top:46px;color:var(--teal);font-size:26px}
.footer .about{left:56px;top:120px;width:310px;font-size:11px;line-height:17px;color:#aaa}
.footer .reg{left:56px;top:224px;font-size:11px;line-height:19px;color:var(--white)}
.footer .reg b{color:var(--teal);font-weight:400}
.footer .addr{left:56px;top:250px;display:flex;font-size:11px;line-height:15px}
.footer .addr .lines{color:var(--teal);margin-left:14px}
.footer h4{font-size:16px;font-weight:600;color:var(--white)}
.links{list-style:none}
.links li{display:flex;align-items:center;gap:14px;font-size:13px}
.links li::before{content:"";width:6px;height:6px;border-right:1.5px solid #ccc;border-top:1.5px solid #ccc;transform:rotate(45deg)}
.quick{left:560px;top:46px}
.quick .links{margin-top:50px}
.quick .links li{height:42px}
.svc{left:876px;top:46px}
.svc .links{margin-top:52px}
.svc .links li{height:27.6px}
.copyright{left:0;top:2928px;width:1200px;height:52px;background:var(--footer-base);color:#cfcfcf;font-size:13px;display:flex;align-items:center;justify-content:center}
</style>
</head>
<body>

<div class="abs topbar">
  <div class="abs address">
    <svg width="10" height="13" viewBox="0 0 10 13"><path d="M5 0a5 5 0 0 0-5 5c0 3.5 5 8 5 8s5-4.5 5-8a5 5 0 0 0-5-5zm0 7a2 2 0 1 1 0-4 2 2 0 0 1 0 4z" fill="#cfcfcf"/></svg>
    Cedar Plaza building, Harbor Free Zone, Al Marsa, U.A.E.
  </div>
  <div class="abs social">
    <span style="background:#3b5998"></span><span style="background:#2aa4de"></span><span style="background:#d9473a"></span><span style="background:#2a78b0"></span><span style="background:#c8232c"></span>
  </div>
</div>

<header class="abs header">
  <div class="abs brand"><span class="mark"></span>Learning Horizon Collective</div>
  <nav class="abs nav"><span>About us</span><span>Our people</span><span>Our services</span><span>Our work</span><span>Contact us</span></nav>
</header>

<section class="abs hero" role="img" aria-label="Photo of a student writing at a classroom desk with classmates behind">
  <h1 class="abs">Lorem ipsum dolor sit arm<br>etconsectetuer adipis</h1>
  <a class="abs btn btn-fill">Read more</a>
  <div class="abs dots"><span></span><span class="on"></span><span></span></div>
</section>

<section class="abs services">
  <h2 class="abs section-title">Our services</h2>
  <div class="abs rule"></div>
  <p class="abs intro">Learning Horizon Collective design, deliver and support Government education systems, public and private universities, groups of private schools, individual schools.</p>

  <div class="abs service" style="left:4px">
    <svg viewBox="0 0 100 116" width="100"><circle cx="50" cy="20" r="18" fill="#8a8a8a"/><path d="M20 60q30-22 60 0v34H20z" fill="#8a8a8a"/><path d="M6 62l44 14 44-14v44l-44 10-44-10z" fill="#8a8a8a"/><path d="M50 76v40" stroke="#f1f1f1" stroke-width="3"/></svg>
    Education Reform
  </div>
  <div class="abs service" style="left:330px">
    <svg viewBox="0 0 120 116" width="120"><circle cx="60" cy="12" r="10" fill="#8a8a8a"/><path d="M44 26h32l6 20H38z" fill="#8a8a8a"/><rect x="40" y="50" width="40" height="30" fill="#8a8a8a"/><circle cx="60" cy="64" r="6" fill="#f1f1f1"/><circle cx="22" cy="84" r="9" fill="#8a8a8a"/><circle cx="98" cy="84" r="9" fill="#8a8a8a"/><rect x="10" y="96" width="24" height="20" fill="#8a8a8a"/><rect x="48" y="88" width="24" height="28" fill="#8a8a8a"/><rect x="86" y="96" width="24" height="20" fill="#8a8a8a"/></svg>
    Teacher training design<br>and delivery
  </div>
  <div class="abs service" style="left:658px">
    <svg viewBox="0 0 150 116" width="150"><path d="M75 2v20" stroke="#8a8a8a" stroke-width="3"/><path d="M75 2h18l-4 6 4 6H75z" fill="#8a8a8a"/><path d="M40 46l35-26 35 26z" fill="#8a8a8a"/><rect x="4" y="46" width="142" height="70" fill="#8a8a8a"/><g fill="#f1f1f1"><rect x="16" y="58" width="14" height="14"/><rect x="38" y="58" width="14" height="14"/><rect x="98" y="58" width="14" height="14"/><rect x="120" y="58" width="14" height="14"/><rect x="16" y="84" width="14" height="14"/><rect x="38" y="84" width="14" height="14"/><rect x="98" y="84" width="14" height="14"/><rect x="120" y="84" width="14" height="14"/><rect x="64" y="80" width="22" height="36"/><circle cx="75" cy="60" r="8"/></g></svg>
    School improvement<br>planning
  </div>
  <div class="abs service" style="left:954px">
    <svg viewBox="0 0 116 116" width="116"><rect x="20" y="40" width="92" height="66" fill="#8a8a8a"/><rect x="4" y="104" width="112" height="8" fill="#8a8a8a"/><circle cx="34" cy="34" r="30" fill="#8a8a8a"/><circle cx="34" cy="34" r="22" fill="#f1f1f1"/><path d="M34 18v16l10 8" stroke="#8a8a8a" stroke-width="4" fill="none"/></svg>
    Curriculum
  </div>

  <a class="abs btn btn-fill">VIEW MORE</a>
</section>

<section class="mission">
  <h2 class="abs">Mission and Philosophy of<br>Learning Horizon Collective</h2>
  <p class="abs body">The Partners have extensive international educational consultancy experience and have worked extensively improving schools, universities, education systems with delivery in the following countries:</p>
  <p class="abs countries">United Kingdom, Australia, Germany, United States, Bahrain, U.A.E, Pakistan, India, South Africa, Saudi Arabia, Jordan.</p>
  <a class="abs btn btn-line">Read more</a>
  <div class="abs photo" role="img" aria-label="Photo of a smiling woman in a patterned headscarf holding a stack of books outdoors"></div>
</section>

<section class="abs band" role="img" aria-label="Darkened photo of students in a classroom behind the call to action">
  <h2 class="abs">Lorem ipsum dolor sit armet</h2>
  <p class="abs">orem ipsum dolor sit armeng elit</p>
  <a class="abs btn btn-fill">REGISTER NOW</a>
</section>

<section class="people">
  <h2 class="abs section-title">Our People</h2>
  <div class="abs rule"></div>
  <div class="abs arrow-btn" style="left:1030px"><svg width="26" height="10" viewBox="0 0 26 10"><path d="M26 5H2M6 1L2 5l4 4" stroke="#777" stroke-width="1.5" fill="none"/></svg></div>
  <div class="abs arrow-btn" style="left:1092px"><svg width="26" height="10" viewBox="0 0 26 10"><path d="M0 5h24M20 1l4 4-4 4" stroke="#777" stroke-width="1.5" fill="none"/></svg></div>
  <div class="abs tabs"><span class="active">Partner A</span><span>Partner B</span></div>

  <div class="abs feature-bg"></div>
  <div class="abs feature-photo" role="img" aria-label="Photo of a teacher at a chalkboard with students raising hands"></div>
  <p class="abs quote feature-quote">Lorem ipsum dolor sit amet, conse ctetuer adipiscing elit, sed diam</p>
  <p class="abs name feature-name">Daniel Morrow</p>

  <div class="abs thumb" style="top:2108px;background:linear-gradient(135deg,#b8b2a8,#e6e2dc 60%,#9a8e86)" role="img" aria-label="Portrait photo of a man in a red checked headdress"></div>
  <p class="abs quote person-quote" style="top:2114px">Lorem ipsum dolor sit amet, conse ctetuer adipiscing elit, sed diam</p>
  <p class="abs name" style="left:816px;top:2184px">Daniel Morrow</p>

  <div class="abs thumb" style="top:2262px;background:linear-gradient(135deg,#a6d2dd,#e2c9a8 55%,#7fb8c8)" role="img" aria-label="Portrait photo of a smiling young woman reading"></div>
  <p class="abs quote person-quote" style="top:2268px">Lorem ipsum dolor sit amet, conse ctetuer adipiscing elit, sed diam</p>
  <p class="abs name" style="left:816px;top:2338px">Daniel Morrow</p>

  <div class="abs thumb" style="top:2412px;background:linear-gradient(135deg,#2a2a2a,#b89a86 55%,#d9d4cf)" role="img" aria-label="Portrait photo of a woman in a black headscarf reading"></div>
  <p class="abs quote person-quote" style="top:2420px">Lorem ipsum dolor sit amet, conse ctetuer adipiscing elit, sed diam</p>
  <p class="abs name" style="left:816px;top:2490px">Daniel Morrow</p>
</section>

<footer class="abs footer">
  <div class="abs brand"><span class="mark"></span>Learning Horizon Collective</div>
  <p class="abs about">The Partners have extensive experience in large-scale education reform across the K-12 and higher education sectors. These experiences have included work within advanced and emerging economy countries, as well systems with more than 50,000 schools.</p>
  <p class="abs reg"><b>Operating Name :</b> Learning Horizon Collective FZC</p>
  <div class="abs addr"><span>Address &nbsp;&nbsp;&nbsp;&nbsp;:</span><span class="lines">Suite Center,<br>Cedar Plaza Building,<br>Harbor Free Zone,<br>Al Marsa, U.A.E.</span></div>

  <div class="abs quick">
    <h4>Quick Links</h4>
    <ul class="links"><li>About us</li><li>Our people</li><li>Our services</li><li>Our work</li><li>Contact us</li></ul>
  </div>
  <div class="abs svc">
    <h4>Our services</h4>
    <ul class="links"><li>School improvement planning</li><li>Education reform</li><li>Teacher training design and delivery</li><li>Curriculum</li><li>Assessment</li><li>School leadership training</li><li>School inspection</li><li>Instructional supervision</li></ul>
  </div>
</footer>
<div class="abs copyright">©copyright 2017 All Rights Reserved</div>

</body>
</html>
```